Poster Required for Cafe to promote coffee/staff discounts

Need an A3 size poster designed for our business to promote that we roast our own coffee, and that we offer discounts for staff.
I have attached a poster which we use to promote catering that our business offers, also have attached logos and our business card..
Also, I have attached our business card I would like the poster to look a little like that.
Eg. Our logo.
Then Specialty Coffee Roasters (under or next to this, in small print: Producing Slow Roasted Coffee)
Location
Download our App
Website
I would like the poster to state:
Tarrindale Health Staff receive $1 off their coffee or hot drink when presenting their staff pass.
Please don't hesitate to ask if you need more info.

```html
<!DOCTYPE html>
<html lang="en">
<head>
<meta charset="utf-8">
<title>Night Shift – Specialty Coffee Roasters</title>
<link rel="stylesheet" href="https://fonts.googleapis.com/css2?family=Oswald:wght@300;400;500&display=swap">
<style>
  :root {
    --paper: #f8f4ad;
    --ink: #5b5a52;
    --ink-soft: #7a786c;
    --badge: #1f1f1f;
    --badge-text: #f4f2e6;
  }
  * { margin: 0; padding: 0; box-sizing: border-box; }
  html, body { width: 849px; height: 1200px; overflow: hidden; background: var(--paper); }
  .poster {
    position: relative; width: 849px; height: 1200px;
    background: var(--paper); color: var(--ink);
    font-family: "Oswald", sans-serif; text-align: center;
  }
  .brand-badge {
    position: absolute; left: 234px; top: 22px; width: 380px; height: 380px;
    border-radius: 50%; background: var(--badge);
  }
  .brand-name {
    position: absolute; left: 0; right: 0; top: 124px;
    font-size: 56px; font-weight: 300; letter-spacing: 6px; line-height: 68px;
    color: var(--badge-text);
  }
  .headline { position: absolute; left: 0; right: 0; top: 478px; font-size: 50px; font-weight: 500; letter-spacing: 2px; }
  .tagline { position: absolute; left: 0; right: 0; top: 550px; font-size: 25px; font-weight: 300; letter-spacing: 4px; color: var(--ink-soft); }
  .bean-row { position: absolute; left: 254px; width: 340px; height: 10px; border-radius: 5px; background: var(--ink-soft); opacity: .55; }
  .bean-row.first { top: 608px; }
  .bean-row.second { top: 754px; }
  .location { position: absolute; left: 0; right: 0; top: 652px; font-size: 27px; font-weight: 300; letter-spacing: 4px; line-height: 44px; color: var(--ink-soft); }
  .app-button {
    position: absolute; left: 318px; top: 790px; width: 212px; height: 60px;
    border: 2px solid var(--ink); font-size: 21px; line-height: 56px; letter-spacing: 1px;
  }
  .website { position: absolute; left: 0; right: 0; top: 896px; font-size: 22px; font-weight: 300; letter-spacing: 2px; }
  .offer-band {
    position: absolute; left: 30px; top: 962px; width: 790px; height: 196px;
    border: 3px solid var(--ink); border-radius: 98px;
  }
  .offer-icon { position: absolute; left: 26px; top: 17px; width: 156px; height: 156px; border-radius: 50%; background: var(--ink); }
  .offer-text {
    position: absolute; left: 192px; right: 20px; top: 46px;
    font-size: 24px; line-height: 48px; letter-spacing: 0.5px; text-align: center;
  }
  .offer-line { display: block; white-space: nowrap; }
</style>
</head>
<body>
<main class="poster">
  <div class="brand-badge">
    <div class="brand-name">NIGHT<br>SHIFT</div>
  </div>

  <h1 class="headline">SPECIALTY COFFEE ROASTERS</h1>
  <p class="tagline">PRODUCING SLOW ROASTED COFFEE</p>

  <div class="bean-row first" role="img" aria-label="Row of small coffee bean ornaments"></div>
  <p class="location">LOCATED AT MARLOW HOSPITAL<br>TARRINDALE, AUSTRALIA</p>
  <div class="bean-row second" role="img" aria-label="Row of small coffee bean ornaments"></div>

  <div class="app-button">DOWNLOAD OUR APP</div>
  <p class="website">NIGHTSHIFTCOFFEE.COM.AU</p>

  <section class="offer-band">
    <div class="offer-icon" role="img" aria-label="Round badge with a steaming hot drink cup icon"></div>
    <p class="offer-text">
      <span class="offer-line">TARRINDALE HEALTH STAFF RECEIVE $1 OFF YOUR COFFEE OR</span>
      <span class="offer-line">HOT DRINK WHEN YOU PRESENT YOUR STAFF PASS</span>
    </p>
  </section>
</main>
</body>
</html>
```